Corporate Design für Apotheke
Zielgruppe
Gesundheitswesen, Apotheke Zielgruppe kranke Menschen aber auch 'shopper'.
Aufgabenstellung
Das alte Logo ist leider viel zu filigran. Bei verschiedenen Druck kommt es oft nicht raus. Früher war das Logo eckig, es wurde vor Jahren mal als rund modernisiert.
Bin aber offen für alles.
Apotheke sollte grundsätzlich mit den Werten Seriosität, Vertrauen , und in unserem Fall auch Exklusivität, Premium- Segment verbunden werden. Im Anhang unser altes Logo. Ich bin zum ersten mal hier und freue mich auf kreative Vorschläge

```html
<!DOCTYPE html>
<html lang="de">
<head>
<meta charset="utf-8">
<title>Talgrund Apotheke – Visitenkarten</title>
<link href="https://fonts.googleapis.com/css2?family=Jost:wght@400;600;700&family=Caveat:wght@400&display=swap" rel="stylesheet">
<style>
  :root {
    --bg: #e4e5e4;
    --green-deep: #1f6f45;
    --green-brand: #2a8052;
    --green-soft: #3b8d66;
    --green-light: #4cae4f;
    --green-faint: #d6e8dc;
    --paper: #ffffff;
    --white: #ffffff;
  }
  * { margin: 0; padding: 0; box-sizing: border-box; }
  html, body { width: 1200px; height: 2190px; overflow: hidden; background: var(--bg); }
  body { position: relative; font-family: "Jost", sans-serif; }

  .card {
    position: absolute;
    left: 199px;
    width: 798px;
    height: 483px;
    overflow: hidden;
  }
  .card--front { top: 195px; background: linear-gradient(135deg, var(--green-brand), var(--green-soft)); color: var(--white); }
  .card--back { background: var(--paper); color: var(--green-deep); }
  .card--back-a { top: 813px; }
  .card--back-b { top: 1428px; }

  /* front */
  .front-mark {
    position: absolute; left: 336px; top: 98px;
    width: 122px; height: 122px;
    border: 5px solid var(--white); border-radius: 50%;
  }
  .front-name {
    position: absolute; left: 0; right: 0; top: 250px;
    text-align: center; font-weight: 700; font-size: 38px;
    letter-spacing: 4px; line-height: 1;
  }
  .front-tagline {
    position: absolute; left: 0; right: 0; top: 300px;
    text-align: center; font-family: "Caveat", cursive; font-size: 44px; line-height: 1;
  }

  /* back */
  .holder-name {
    position: absolute; left: 59px;
    font-weight: 700; font-size: 34px; letter-spacing: 1.5px; line-height: 1;
    color: var(--green-deep);
  }
  .holder-rule { position: absolute; left: 59px; height: 3px; background: var(--green-light); }
  .holder-role {
    position: absolute; left: 59px; font-size: 23px; line-height: 1;
    color: var(--green-light);
  }
  .contact { position: absolute; font-size: 25px; line-height: 38px; color: var(--green-deep); }
  .contact p { white-space: nowrap; }
  .contact .gap { height: 28px; }
  .contact b { font-weight: 600; display: inline-block; width: 82px; }

  .card--back-a .holder-name { top: 50px; }
  .card--back-a .holder-rule { top: 111px; width: 514px; }
  .card--back-a .holder-role { top: 128px; }
  .card--back-a .contact { left: 246px; top: 222px; }

  .card--back-b .holder-name { top: 68px; }
  .card--back-b .holder-rule { top: 117px; width: 667px; }
  .card--back-b .holder-role { top: 142px; }
  .card--back-b .contact { left: 266px; top: 226px; }

  .brand-mark {
    position: absolute; left: 619px; top: 51px;
    width: 122px; height: 122px;
    border: 5px solid var(--green-deep); border-radius: 50%;
    display: flex; align-items: center; justify-content: center;
    font-weight: 600; font-size: 17px; letter-spacing: 1px; color: var(--green-deep);
  }
  .brand-ghost { position: absolute; left: -64px; top: 282px; }
</style>
</head>
<body>

  <section class="card card--front">
    <div class="front-mark"></div>
    <div class="front-name">TALGRUND APOTHEKE</div>
    <div class="front-tagline">Gesundheit mitten in Talheim</div>
  </section>

  <section class="card card--back card--back-a">
    <h1 class="holder-name">JONAS BEISPIEL</h1>
    <div class="holder-rule"></div>
    <p class="holder-role">Fachapotheker für Onkologie</p>
    <div class="brand-mark">TALGRUND</div>
    <div class="contact">
      <p>Talgrund Apotheke</p>
      <p>Lindenweg 1 | 79999 Talheim</p>
      <div class="gap"></div>
      <p><b>Fon:</b>012 345 77 00</p>
      <p><b>Web:</b>talgrund-apotheke.de</p>
      <p><b>Mail:</b>info@talgrund-apotheke.de</p>
    </div>
  </section>

  <section class="card card--back card--back-b">
    <h1 class="holder-name">JONAS BEISPIEL</h1>
    <div class="holder-rule"></div>
    <p class="holder-role">Fachapotheker für Onkologie</p>
    <svg class="brand-ghost" width="250" height="250" viewBox="0 0 250 250" aria-hidden="true">
      <circle cx="125" cy="125" r="118" fill="none" stroke="var(--green-faint)" stroke-width="8"/>
    </svg>
    <div class="contact">
      <p>Talgrund Apotheke</p>
      <p>Lindenweg 1 | 79999 Talheim</p>
      <div class="gap"></div>
      <p><b>Fon:</b>012 345 77 00</p>
      <p><b>Web:</b>talgrund-apotheke.de</p>
      <p><b>Mail:</b>info@talgrund-apotheke.de</p>
    </div>
  </section>

</body>
</html>
```